Geschäftspapiere für Malerfirma
Zielgruppe
Malerfirma für hochwertige Kundschaft.
Wir verarbeiten besondes hochpigmentierte Farben und hochwertigen Tapeten.
Aufgabenstellung
Unser neues Motto ist ,, Aus Liebe zu unserer Berufung'
Wir führen viele Tapezierarbeiten aus ... etwas mit einem Tapetenmuster (Muster aus dem Firmenlogo) finde ich schon ansprechend.

```html
<!DOCTYPE html>
<html lang="de">
<head>
<meta charset="utf-8">
<title>Briefbogen – Jonas Keller Malermeister</title>
<link href="https://fonts.googleapis.com/css2?family=Open+Sans:wght@300;400;600&display=swap" rel="stylesheet">
<style>
  :root {
    --bg: #d6d4d5;
    --paper: #f2f2f2;
    --paper-shade: #ebebeb;
    --green: #6e9c3e;
    --green-dark: #5e8c32;
    --maroon: #7b4b57;
    --maroon-dark: #6c3f4b;
    --brown-text: #8c6b66;
    --ink: #2b2222;
    --watermark: #e3e3e3;
    --swoosh-grey: #dcdcdc;
    --white: #ffffff;
  }
  * { margin: 0; padding: 0; box-sizing: border-box; }
  html, body { width: 1119px; height: 1200px; overflow: hidden; }
  body {
    background: var(--bg);
    font-family: "Open Sans", Arial, sans-serif;
    position: relative;
  }
  .letterhead {
    position: absolute;
    left: 158px;
    top: 35px;
    width: 862px;
    height: 1215px;
    transform: scale(0.93);
    transform-origin: top left;
    background: linear-gradient(180deg, var(--paper) 0%, var(--paper-shade) 100%);
    overflow: hidden;
  }
  .header-art, .footer-art { position: absolute; left: 0; width: 862px; display: block; }
  .header-art { top: 0; height: 170px; }
  .footer-art { top: 1065px; height: 150px; }
  .brand {
    position: absolute;
    left: 80px;
    top: 62px;
    color: var(--white);
    font-weight: 600;
    font-size: 28px;
    line-height: 36px;
    letter-spacing: 0.3px;
    white-space: nowrap;
  }
  .sender-line {
    position: absolute;
    left: 62px;
    top: 209px;
    font-size: 11.5px;
    color: var(--ink);
    white-space: nowrap;
  }
  .sender-line .sender-name { color: var(--brown-text); }
  .contact-block {
    position: absolute;
    left: 622px;
    top: 207px;
    color: var(--ink);
    white-space: nowrap;
  }
  .contact-name { font-size: 15px; color: var(--brown-text); line-height: 20px; }
  .contact-address {
    display: inline-block;
    font-size: 13.5px;
    line-height: 18px;
    padding: 0 4px 3px 0;
    border-bottom: 1px solid #b79d98;
    margin-bottom: 8px;
  }
  .contact-list { list-style: none; font-size: 13px; }
  .contact-list li { display: flex; align-items: center; gap: 8px; height: 18px; }
  .contact-list svg { width: 16px; height: 12px; fill: var(--brown-text); flex: none; }
  .watermark {
    position: absolute;
    left: 90px;
    top: 545px;
    width: 600px;
    text-align: center;
    color: var(--watermark);
    font-weight: 300;
    font-size: 120px;
    line-height: 120px;
  }
  .tax-info {
    position: absolute;
    left: 62px;
    top: 1138px;
    font-size: 13px;
    line-height: 18px;
    color: var(--ink);
    white-space: nowrap;
  }
</style>
</head>
<body>
<main class="letterhead">
  <svg class="header-art" viewBox="0 0 862 170">
    <defs>
      <linearGradient id="greenBand" x1="0" y1="0" x2="1" y2="1">
        <stop offset="0" stop-color="var(--green)"/>
        <stop offset="1" stop-color="var(--green-dark)"/>
      </linearGradient>
      <path id="mottoCurve" d="M278 60 C400 38 520 40 632 72"/>
    </defs>
    <path role="img" aria-label="Grünes Tapetenmuster mit Ornamenten" fill="url(#greenBand)"
          d="M0 0 H862 V160 C760 110 620 80 470 78 C300 76 120 100 0 125 Z"/>
    <path class="swoosh" fill="var(--maroon)"
          d="M0 112 C150 88 380 72 560 86 C400 82 200 104 0 152 Z"/>
    <text font-family="Open Sans, Arial, sans-serif" font-size="19" fill="var(--white)">
      <textPath href="#mottoCurve">„Aus Liebe zu unserer Berufung „</textPath>
    </text>
  </svg>

  <div class="brand">Jonas Keller</div>

  <p class="sender-line"><span class="sender-name">JONAS KELLER |</span> Lindenweg 48 * 10435 Berlin</p>

  <section class="contact-block">
    <p class="contact-name">Jonas Keller</p>
    <p class="contact-address">Lindenweg 48 *10435 Berlin</p>
    <ul class="contact-list">
      <li><svg viewBox="0 0 16 12"><path d="M1 4 C1 1 15 1 15 4 L12 5 L11 3 H5 L4 5 Z M4 6 H12 L14 11 H2 Z"/></svg>030/48291756</li>
      <li><svg viewBox="0 0 16 12"><path d="M4 0 H12 V4 H4 Z M1 5 H15 V10 H1 Z M4 8 H12 V12 H4 Z"/></svg>030/48291758</li>
      <li><svg viewBox="0 0 16 12"><path d="M5 0 H11 V12 H5 Z M6 1 V10 H10 V1 Z"/></svg>0176/59138402</li>
      <li><svg viewBox="0 0 16 12"><path d="M1 1 H15 L8 7 Z M1 3 L8 9 L15 3 V11 H1 Z"/></svg>malermeister-keller@mailpost.de</li>
    </ul>
  </section>

  <p class="watermark" aria-hidden="true">Jonas<br>Keller</p>

  <p class="tax-info">USt-IdNr.:DE918264530<br>Steuernummer 147/318/00921</p>

  <svg class="footer-art" viewBox="0 0 862 150">
    <path fill="var(--swoosh-grey)" d="M0 116 C400 110 700 62 862 -4 V6 C700 72 400 118 0 125 Z"/>
    <path role="img" aria-label="Weinrotes Tapetenmuster mit Ornamenten" fill="var(--maroon)"
          d="M862 4 C700 72 400 120 0 127 V150 H862 Z"/>
  </svg>
</main>
</body>
</html>
```